Name Card, Stationary, Warranty Seal, Receipt Book
Qorvix Repair Centre
Simple
Tomas
27 Wexley Lane #08-04
Singapore 58817
qrv@qorvix-mail.test
www.qorvix-fix.test
State in we Repair veltra, Plumstone, Korvane and others Smart Phones
On the spot Repair.
For this you are able to use your creative base on our line of repair service

```html
<!DOCTYPE html>
<html lang="en">
<head>
<meta charset="utf-8">
<title>Qorvix Repair Centre – Name Cards</title>
<link href="https://fonts.googleapis.com/css2?family=Arimo:wght@400;700&display=swap" rel="stylesheet">
<style>
  :root {
    --stage: #2b2b2b;
    --card: #ffffff;
    --orange: #f07a1a;
    --orange-deep: #d85c0c;
    --blue: #1f5fa8;
    --navy: #1d3f73;
    --grey: #6a6a6a;
    --line: #c9c9c9;
    --faint: #e6edf5;
  }
  * { box-sizing: border-box; margin: 0; padding: 0; }
  html, body { width: 1200px; height: 963px; overflow: hidden; }
  body { background: var(--stage); font-family: "Arimo", Arial, sans-serif; position: relative; }

  .card {
    position: absolute; left: 429px; width: 344px; height: 200px;
    background: var(--card); border-radius: 12px; overflow: hidden;
  }
  .card--front { top: 156px; }
  .card--alt { top: 385px; }
  .card--back { top: 609px; }

  .band {
    position: absolute; left: 0; right: 0; bottom: 0; height: 16px;
    background: linear-gradient(to bottom, var(--orange), var(--orange-deep));
  }
  .band--thin { height: 5px; }

  .brand { position: absolute; display: flex; align-items: center; gap: 6px; }
  .brand__dot { width: 26px; height: 26px; border-radius: 50%; background: var(--orange); flex: none; }
  .brand__text { display: flex; flex-direction: column; line-height: 1; }
  .brand__name { font-weight: 700; font-size: 26px; color: var(--blue); letter-spacing: 0.5px; }
  .brand__sub { font-weight: 700; font-size: 9px; color: var(--blue); letter-spacing: 1.2px; margin-top: 3px; }

  .watermark {
    position: absolute; left: -30px; top: 10px; width: 120px; height: 120px;
    border-radius: 50%; background: var(--faint);
  }

  .holder { position: absolute; line-height: 1.35; }
  .holder__name { font-size: 20px; }
  .holder__addr { font-size: 10px; }

  .contacts { position: absolute; font-size: 8px; line-height: 1.45; border-collapse: collapse; }
  .contacts th { font-weight: 400; text-align: left; padding-right: 10px; }
  .contacts td { padding: 0; }

  .card--front .brand { right: 14px; top: 18px; }
  .card--front .holder { left: 14px; top: 92px; color: var(--blue); }
  .card--front .contacts { left: 196px; top: 102px; color: var(--blue); }

  .card--alt .brand { left: 14px; top: 62px; flex-direction: column; align-items: center; gap: 6px; }
  .card--alt .brand__text { align-items: center; }
  .card--alt .divider { position: absolute; left: 176px; top: 38px; width: 1px; height: 120px; background: var(--line); }
  .card--alt .holder { left: 192px; top: 44px; }
  .card--alt .holder__name { color: var(--orange); font-size: 22px; }
  .card--alt .holder__addr { color: var(--orange-deep); }
  .card--alt .contacts { left: 192px; top: 106px; color: var(--grey); }

  .card--back .brand { left: 50%; top: 72px; transform: translateX(-50%); }
  .card--back .url {
    position: absolute; right: 16px; bottom: 3px; font-size: 8px; color: #fff;
  }
</style>
</head>
<body>

  <section class="card card--front" aria-label="Name card front">
    <div class="watermark"></div>
    <div class="brand">
      <span class="brand__dot"></span>
      <span class="brand__text">
        <span class="brand__name">Qorvix</span>
        <span class="brand__sub">REPAIR CENTRE</span>
      </span>
    </div>
    <div class="holder">
      <p class="holder__name">Tomas</p>
      <p class="holder__addr">27 Wexley Lane #08-04</p>
      <p class="holder__addr">Singapore 58817</p>
    </div>
    <table class="contacts">
      <tr><th>Phone</th><td>6555 0142</td></tr>
      <tr><th>Fax</th><td>6555 0143</td></tr>
      <tr><th>Email</th><td>qrv@qorvix-mail.test</td></tr>
      <tr><th>Web</th><td>www.qorvix-fix.test</td></tr>
    </table>
    <div class="band"></div>
  </section>

  <section class="card card--alt" aria-label="Name card alternate">
    <div class="brand">
      <span class="brand__dot"></span>
      <span class="brand__text">
        <span class="brand__name">Qorvix</span>
        <span class="brand__sub">REPAIR CENTRE</span>
      </span>
    </div>
    <div class="divider"></div>
    <div class="holder">
      <p class="holder__name">Tomas</p>
      <p class="holder__addr">27 Wexley Lane #08-04</p>
      <p class="holder__addr">Singapore 58817</p>
    </div>
    <table class="contacts">
      <tr><th>Phone</th><td>6555 0142</td></tr>
      <tr><th>Fax</th><td>6555 0143</td></tr>
      <tr><th>Email</th><td>qrv@qorvix-mail.test</td></tr>
      <tr><th>Web</th><td>www.qorvix-fix.test</td></tr>
    </table>
    <div class="band band--thin"></div>
  </section>

  <section class="card card--back" aria-label="Name card back">
    <div class="brand">
      <span class="brand__dot"></span>
      <span class="brand__text">
        <span class="brand__name">Qorvix</span>
        <span class="brand__sub">REPAIR CENTRE</span>
      </span>
    </div>
    <div class="band"></div>
    <p class="url">http://www.qorvix-fix.test</p>
  </section>

</body>
</html>
```